Brisk Hive 360 Postcard Design, Double-Sided

Please read carefully and see attached. Designers that do not follow these instructions will not be selected. Limit ONE design submission per artist. The ONE design submission shall show both the front and the back designs. Designs must comply with the attached dismensions accounting for the bleed area to prevent designs from being cut off during printing. The attached business card and door tag designs have already been created, printed and are in use. The postcard shall be similar in design to the attached business card and door tag. All of the information that you need is attached. The overall size is 4.12" x 6.12" for the front. The back is different, see attached and scale to match template. I would like the Veteran Owned Business logo added as well. It would also be nice to see my photo incorporated somehow. I like the yellow on the door tag. It helps build contrast and pops out. Again, one design submission per designer that shows both the front and the back.

Target Market(s)

Please read all instructions and see attached.

Industry/Entity Type

Requirements
Must have
• Please read all instructions and see attached.
Nice to have
Should not have

```html
<!DOCTYPE html>
<html lang="en">
<head>
<meta charset="utf-8">
<title>Brisk Hive 360 Postcard – Front and Back</title>
<link rel="stylesheet" href="https://fonts.googleapis.com/css2?family=Poppins:wght@700;800&family=Oswald:wght@400;500;600;700&display=swap">
<style>
  :root{
    --ink:#0b0b0b;
    --panel:#1b1b1b;
    --paper:#ffffff;
    --yellow:#f2e61c;
    --stage:#7c7c7c;
    --seal:#d9d9d9;
  }
  *{box-sizing:border-box;margin:0;padding:0}
  html,body{width:1122px;height:1200px;overflow:hidden;background:var(--stage)}
  .canvas{position:relative;width:1122px;height:1200px}
  .card{position:absolute;left:131px;width:860px;height:570px;overflow:hidden;box-shadow:0 4px 14px rgba(0,0,0,.25)}
  .card--front{top:20px;background:var(--paper)}
  .card--back{top:610px;background:var(--paper)}
  .layer{position:absolute;left:0;top:0}

  /* front */
  .front-title{position:absolute;left:0;right:0;top:22px;text-align:center;font-family:"Poppins",sans-serif;font-weight:800;font-size:74px;line-height:1;color:var(--paper);letter-spacing:1px}
  .front-rule{position:absolute;left:150px;width:580px;top:104px;height:3px;background:var(--yellow)}
  .front-trade{position:absolute;left:0;right:0;top:112px;text-align:center;font-family:"Poppins",sans-serif;font-weight:800;font-size:38px;color:var(--yellow);letter-spacing:1px}
  .front-mark{position:absolute;left:0;right:0;top:208px;display:flex;justify-content:center;align-items:center;gap:10px;font-family:"Oswald",sans-serif;font-weight:600;font-size:26px;color:var(--paper)}
  .mark-dot{width:18px;height:18px;border-radius:50%;background:var(--yellow)}
  .gallery{position:absolute;left:64px;right:64px;top:343px;display:flex;justify-content:space-between}
  .gallery-frame{width:224px;height:158px;border:4px solid var(--ink);background:var(--paper);padding:7px}
  .gallery-photo{width:100%;height:100%}
  .photo-doorbell{background:linear-gradient(90deg,#5d5650 0 38%,#c9ccd0 38% 80%,#2a2a2a 80%)}
  .photo-hardware{background:radial-gradient(circle at 50% 55%,#c9a640 0 18%,#e9eef3 45%)}
  .photo-network{background:radial-gradient(circle at 50% 55%,#5fd8ff 0 12%,#1a64b8 40%,#071a3c 80%)}
  .front-contact{position:absolute;left:0;right:0;top:520px;display:flex;justify-content:center;align-items:center;font-family:"Oswald",sans-serif;font-weight:500;font-size:16px;color:var(--paper)}
  .front-contact .item{display:flex;align-items:center;gap:7px;padding:0 12px}
  .front-contact .item+.item{border-left:2px solid var(--paper)}
  .icon{width:17px;height:17px;flex:none}

  /* back */
  .back-panel{position:absolute;left:0;top:0;width:489px;height:391px;background:var(--panel);overflow:hidden}
  .back-band{position:absolute;left:0;top:391px;width:489px;height:15px;background:var(--yellow)}
  .back-title{position:absolute;left:22px;top:20px;font-family:"Poppins",sans-serif;font-weight:800;font-size:36px;line-height:.98;color:var(--paper)}
  .back-rule{position:absolute;left:22px;top:96px;width:182px;height:2px;background:var(--yellow)}
  .back-trade{position:absolute;left:22px;top:98px;font-family:"Poppins",sans-serif;font-weight:700;font-size:18px;color:var(--paper)}
  .owner-photo{position:absolute;left:226px;top:22px;width:110px;height:148px;border-radius:40px 40px 0 0;background:linear-gradient(180deg,#8c8f94,#c6c9cd)}
  .owner{position:absolute;left:346px;top:34px;font-family:"Oswald",sans-serif;color:var(--paper)}
  .owner-name{font-size:19px;font-weight:600;line-height:1}
  .owner-role{font-size:8px;font-weight:600;color:var(--yellow)}
  .cert-seal{position:absolute;left:203px;top:154px;width:62px;height:62px;border-radius:50%;background:var(--seal)}
  .divider{position:absolute;left:234px;top:216px;width:1px;height:175px;background:var(--paper)}
  .list-block{position:absolute;font-family:"Oswald",sans-serif;color:var(--paper)}
  .list-block--services{left:29px;top:178px}
  .list-block--benefits{left:290px;top:178px}
  .list-heading{font-weight:700;font-size:22px;color:var(--yellow);line-height:1.1}
  .list-sub{font-size:15px;line-height:1.1;margin-bottom:16px}
  .list{list-style:none;font-size:15.5px;margin-top:6px}
  .list li{position:relative;padding-left:20px;height:24px;line-height:24px}
  .list li::before{content:"";position:absolute;left:3px;top:9px;width:7px;height:7px;border-radius:50%;background:var(--paper)}
  .back-contact{position:absolute;left:29px;top:418px;font-family:"Oswald",sans-serif;color:var(--ink)}
  .back-contact h3{font-size:20px;font-weight:700;margin-bottom:6px}
  .back-contact .item{display:flex;align-items:center;gap:10px;font-size:14px;height:26px}
  .back-contact .icon{width:14px;height:14px}
  .stamp-box{position:absolute;left:675px;top:52px;width:131px;height:131px;border:1.5px solid var(--ink)}
</style>
</head>
<body>
<div class="canvas">

  <!-- front side -->
  <section class="card card--front">
    <svg class="layer" width="860" height="570" viewBox="0 0 860 570" aria-hidden="true">
      <polygon points="0,0 860,0 860,208 430,300 0,208" fill="var(--ink)"/>
      <polygon points="0,208 430,300 860,208 860,228 430,320 0,228" fill="var(--yellow)"/>
      <polygon points="0,228 430,320 860,228 860,238 430,330 0,238" fill="var(--ink)"/>
      <rect x="0" y="472" width="860" height="98" fill="var(--ink)"/>
    </svg>
    <h1 class="front-title">BRISK HIVE 360</h1>
    <div class="front-rule"></div>
    <div class="front-trade">HANDYMAN</div>
    <div class="front-mark"><span class="mark-dot"></span>Brisk Hive 360</div>

    <div class="gallery">
      <div class="gallery-frame"><div class="gallery-photo photo-doorbell" role="img" aria-label="Photo of a video doorbell installed beside a stone wall"></div></div>
      <div class="gallery-frame"><div class="gallery-photo photo-hardware" role="img" aria-label="Photo of brass picture-hanging hooks and nails"></div></div>
      <div class="gallery-frame"><div class="gallery-photo photo-network" role="img" aria-label="Illustration of a wireless router connecting home devices"></div></div>
    </div>

    <div class="front-contact">
      <span class="item">
        <svg class="icon" viewBox="0 0 20 20"><circle cx="10" cy="10" r="10" fill="var(--yellow)"/><path d="M6.5 5.5l2 0 1 2.5-1.3 1a6 6 0 0 0 2.8 2.8l1-1.3 2.5 1v2c0 .6-.5 1-1 1A8 8 0 0 1 5.5 6.5c0-.5.4-1 1-1z" fill="var(--ink)"/></svg>
        (555) 014-2290</span>
      <span class="item">
        <svg class="icon" viewBox="0 0 20 20"><circle cx="10" cy="10" r="10" fill="var(--yellow)"/><path d="M10 4a4 4 0 0 0-4 4c0 3 4 8 4 8s4-5 4-8a4 4 0 0 0-4-4z" fill="var(--ink)"/><circle cx="10" cy="8" r="1.6" fill="var(--yellow)"/></svg>
        Bayview, Florida</span>
      <span class="item">
        <svg class="icon" viewBox="0 0 20 20"><circle cx="10" cy="10" r="10" fill="var(--yellow)"/><rect x="5" y="6.5" width="10" height="7" fill="var(--ink)"/><path d="M5 6.5l5 4 5-4" stroke="var(--yellow)" stroke-width="1" fill="none"/></svg>
        Service@BriskHive360.com</span>
      <span class="item">
        <svg class="icon" viewBox="0 0 20 20"><circle cx="10" cy="10" r="10" fill="var(--yellow)"/><g fill="none" stroke="var(--ink)" stroke-width="1.2"><circle cx="10" cy="10" r="5"/><ellipse cx="10" cy="10" rx="2.2" ry="5"/><path d="M5 10h10"/></g></svg>
        BriskHive360.com</span>
    </div>
  </section>

  <!-- back side -->
  <section class="card card--back">
    <div class="back-panel">
      <div class="owner-photo" role="img" aria-label="Photo of the owner in a grey work shirt"></div>
      <svg class="layer" width="489" height="391" viewBox="0 0 489 391" aria-hidden="true">
        <polygon points="0,118 235,170 489,112 489,391 0,391" fill="var(--panel)"/>
        <polyline points="0,118 235,170 489,112" fill="none" stroke="var(--yellow)" stroke-width="5"/>
      </svg>
      <h2 class="back-title">BRISK<br>HIVE 360</h2>
      <div class="back-rule"></div>
      <div class="back-trade">HANDYMAN</div>
      <div class="owner">
        <div class="owner-name">DALEN R. VOSS</div>
        <div class="owner-role">OWNER &amp; HANDYMAN</div>
      </div>
      <div class="cert-seal" role="img" aria-label="Certification seal"></div>
      <div class="divider"></div>

      <div class="list-block list-block--services">
        <div class="list-heading">SERVICES</div>
        <ul class="list">
          <li>Assembly</li>
          <li>Small Repairs</li>
          <li>Wifi / Router Setup</li>
          <li>Fabrication</li>
          <li>Hanging Items</li>
          <li>Wireless Devise Setup</li>
          <li>Odd Jobs</li>
        </ul>
      </div>
      <div class="list-block list-block--benefits">
        <div class="list-heading">BENEFITS</div>
        <div class="list-sub">of using our services</div>
        <ul class="list">
          <li>Fast Response</li>
          <li>High Quality</li>
          <li>Fair Pricing</li>
          <li>Veteran Owned</li>
        </ul>
      </div>
    </div>
    <div class="back-band"></div>

    <div class="back-contact">
      <h3>CONTACT US:</h3>
      <div class="item">
        <svg class="icon" viewBox="0 0 20 20"><circle cx="10" cy="10" r="10" fill="var(--ink)"/><path d="M6.5 5.5l2 0 1 2.5-1.3 1a6 6 0 0 0 2.8 2.8l1-1.3 2.5 1v2c0 .6-.5 1-1 1A8 8 0 0 1 5.5 6.5c0-.5.4-1 1-1z" fill="var(--paper)"/></svg>
        (555) 014-2290</div>
      <div class="item">
        <svg class="icon" viewBox="0 0 20 20"><circle cx="10" cy="10" r="10" fill="var(--ink)"/><path d="M10 4a4 4 0 0 0-4 4c0 3 4 8 4 8s4-5 4-8a4 4 0 0 0-4-4z" fill="var(--paper)"/><circle cx="10" cy="8" r="1.6" fill="var(--ink)"/></svg>
        Bayview, Florida</div>
      <div class="item">
        <svg class="icon" viewBox="0 0 20 20"><circle cx="10" cy="10" r="10" fill="var(--ink)"/><rect x="5" y="6.5" width="10" height="7" fill="var(--paper)"/><path d="M5 6.5l5 4 5-4" stroke="var(--ink)" stroke-width="1" fill="none"/></svg>
        Service@BriskHive360.com</div>
      <div class="item">
        <svg class="icon" viewBox="0 0 20 20"><circle cx="10" cy="10" r="10" fill="var(--ink)"/><g fill="none" stroke="var(--paper)" stroke-width="1.2"><circle cx="10" cy="10" r="5"/><ellipse cx="10" cy="10" rx="2.2" ry="5"/><path d="M5 10h10"/></g></svg>
        BriskHive360.com</div>
    </div>

    <div class="stamp-box"></div>
  </section>

</div>
</body>
</html>
```